Brightwell Trades - ELectrical Contractor Van Wrap

Looking for a new, modernized logo for our new van fleet. (2023 Halvern Courier Full Size)
Brightwell Trades is an electrical contractor in Seattle, focusing on Commercial Electrical, Fire & Security installation, service & inspections. We would like to stick with white/black/grey/red as the color scheme. I added our logo & an image of our current small vans. I do not want them to match perfectly, but be similar. I am not opposed to getting rid of the Flame/Red Circle
Updates

Target Market(s)

Commercial Property Management groups/ Apartment Properties

Industry/Entity Type

Electrical

Colors
EB3D1F
EC4F4E
F09395
F8D3D4
FCEDEE

Requirements
Nice to have
• Modern/simplistic

```html
<!DOCTYPE html>
<html lang="en">
<head>
<meta charset="utf-8">
<title>Brightwell Trades – Van Wrap</title>
<link rel="stylesheet" href="https://fonts.googleapis.com/css2?family=Roboto+Condensed:wght@300;700&family=Poppins:wght@500;600&display=swap">
<style>
  :root {
    --wrap-white: #f4f4f4;
    --brand-red: #e3262a;
    --ink-grey: #4a4a4c;
    --band-dark: #2f2f31;
    --stage: #ffffff;
    --text-light: #ffffff;
  }
  * { margin: 0; padding: 0; box-sizing: border-box; }
  html, body {
    width: 1200px; height: 1200px; overflow: hidden;
    background: var(--stage);
  }
  .wrap-panel {
    position: absolute; left: 40px; top: 380px;
    width: 1120px; height: 440px;
    background: var(--wrap-white);
    border-radius: 18px;
    overflow: hidden;
    box-shadow: 0 0 0 1px #dcdcdc;
  }
  .red-band {
    position: absolute; left: 0; top: 270px;
    width: 100%; height: 80px;
    background: var(--brand-red);
  }
  .service-band {
    position: absolute; left: 0; top: 350px;
    width: 100%; height: 90px;
    background: var(--band-dark);
  }
  .brand-circle {
    position: absolute; left: 770px; top: -6px;
    width: 336px; height: 336px;
    border-radius: 50%;
    background: var(--brand-red);
    box-shadow: 0 0 0 12px var(--wrap-white);
  }
  .wordmark {
    position: absolute; left: 410px; top: 62px;
    font-family: "Roboto Condensed", sans-serif;
    color: var(--ink-grey);
    line-height: 1;
  }
  .wordmark-top {
    font-weight: 300; font-size: 64px; letter-spacing: -1px;
  }
  .wordmark-bottom {
    font-weight: 700; font-size: 72px; letter-spacing: 1px;
    margin-top: 2px;
  }
  .trade-list {
    font-weight: 300; font-size: 24px; letter-spacing: 0.3px;
    margin-top: 8px;
  }
  .web-address {
    position: absolute; left: 170px; top: 299px;
    font-family: "Poppins", sans-serif; font-weight: 500;
    font-size: 18px; color: var(--text-light);
  }
  .phone-number {
    position: absolute; left: 408px; top: 282px;
    font-family: "Poppins", sans-serif; font-weight: 600;
    font-size: 42px; line-height: 1.2; color: var(--text-light);
  }
  .service-list {
    position: absolute; left: 255px; top: 372px;
    font-family: "Poppins", sans-serif; font-weight: 600;
    font-size: 19px; color: var(--text-light);
    display: flex; gap: 10px; align-items: center;
  }
  .service-dot {
    width: 8px; height: 8px; border-radius: 50%;
    background: var(--brand-red);
  }
</style>
</head>
<body>
  <main class="wrap-panel">
    <div class="red-band"></div>
    <div class="service-band"></div>
    <div class="brand-circle"></div>

    <div class="wordmark">
      <div class="wordmark-top">BRIGHTWELL</div>
      <div class="wordmark-bottom">TRADES</div>
      <div class="trade-list">ELECTRICAL | FIRE | SECURITY</div>
    </div>

    <div class="web-address">BRIGHTWELL-TR.COM</div>
    <div class="phone-number">253.555.0142</div>

    <div class="service-list">
      <span>Commercial</span><span class="service-dot"></span>
      <span>Design</span><span class="service-dot"></span>
      <span>Installation</span><span class="service-dot"></span>
      <span>Service</span><span class="service-dot"></span>
      <span>Inspection</span>
    </div>
  </main>
</body>
</html>
```